Meridian Swift add on sales tool2017

This will be a flyer to leave with our clients we just did work for. We want to entice them to use our other services over the next 30 days with a discount, money off etc. we will write in the special and the expiration date. I want the client to read the description and see a picture of the service they may want done.

Target Market(s)

Repeat clients

Industry/Entity Type

Cleaning Service

Font styles to use
Serif
Sans Serif

Colors
ec1f27
000000
b1b1b1

Requirements
Must have
• Call to action! look high end market, clients show we do 1st class work.
• Don't Waite
Nice to have
• Classy, quality, I'm open to using other pictures that may look better
Should not have
• Look like a typical carpet cleaners special flyer
• Not to look cluttered

```html
<!DOCTYPE html>
<html lang="en">
<head>
<meta charset="utf-8">
<title>Meridian Swift – Add-On Services Flyer</title>
<link rel="stylesheet" href="https://fonts.googleapis.com/css2?family=EB+Garamond:wght@700&family=Roboto+Condensed:wght@700&family=Source+Sans+3:wght@400;700&display=swap">
<style>
  :root {
    --brand-red: #ec1f27;
    --ink: #000000;
    --silver: #b1b1b1;
    --paper: #ffffff;
    --photo-dark: #3f4347;
    --photo-light: #efedeb;
    --photo-floor: #d9c9c3;
  }
  * { margin: 0; padding: 0; box-sizing: border-box; }
  html, body { width: 849px; height: 1200px; overflow: hidden; background: var(--ink); }
  .flyer { position: relative; width: 849px; height: 1200px; background: var(--ink); overflow: hidden; }

  .brand { position: absolute; left: 0; top: 44px; width: 100%; text-align: center; }
  .brand-name { font-family: "Source Sans 3", sans-serif; font-weight: 700; font-size: 60px; line-height: 1; color: var(--paper); letter-spacing: 3px; }
  .brand-tagline { font-family: "Source Sans 3", sans-serif; font-weight: 400; font-size: 24px; line-height: 1; margin-top: 14px; color: var(--silver); letter-spacing: 6px; text-transform: uppercase; }

  .headline { position: absolute; top: 182px; left: 0; width: 100%; text-align: center; font-family: "Source Sans 3", sans-serif; font-weight: 700; font-size: 35px; color: #d2d2d2; letter-spacing: 0.2px; }

  .backdrop { position: absolute; inset: 0; }

  .services { position: absolute; left: 424px; top: 380px; list-style: none; }
  .service { display: flex; align-items: center; height: 84px; margin-bottom: 16px; }
  .service-icon { width: 84px; height: 84px; border-radius: 50%; background: var(--paper); border: 3px solid var(--brand-red); display: flex; align-items: center; justify-content: center; flex: none; }
  .service-icon svg { width: 44px; height: 44px; }
  .service-name { margin-left: 23px; font-family: "EB Garamond", serif; font-weight: 700; font-size: 30px; line-height: 1.25; color: var(--ink); }

  .call { position: absolute; left: 424px; top: 908px; display: flex; align-items: center; }
  .call-icon { width: 86px; height: 86px; border-radius: 50%; background: var(--ink); display: flex; align-items: center; justify-content: center; }
  .call-icon svg { width: 46px; height: 46px; }
  .call-text { margin-left: 23px; color: var(--ink); }
  .call-label { font-family: "EB Garamond", serif; font-weight: 700; font-size: 42px; line-height: 0.95; }
  .call-number { font-family: "Roboto Condensed", sans-serif; font-weight: 700; font-size: 52px; line-height: 1; }

  .offer { position: absolute; left: 48px; top: 658px; width: 348px; height: 348px; border-radius: 50%; border: 3px solid var(--paper); padding: 10px; }
  .offer-inner { width: 100%; height: 100%; border-radius: 50%; background: var(--ink); display: flex; flex-direction: column; align-items: center; justify-content: center; color: var(--paper); font-family: "EB Garamond", serif; font-weight: 700; text-align: center; }
  .offer-days { font-size: 54px; line-height: 1; }
  .offer-sub { font-size: 27px; line-height: 1.2; }
  .offer-rule { width: 76px; height: 2px; background: var(--paper); margin: 14px 0 12px; }
  .offer-discount { font-size: 40px; line-height: 1; }
  .offer-note { font-size: 21px; line-height: 1.3; }

  .contact { position: absolute; top: 1104px; left: 0; width: 100%; text-align: center; font-family: "Source Sans 3", sans-serif; color: #bdbdbd; }
  .contact-address { font-size: 20px; }
  .contact-web { font-size: 25px; letter-spacing: 4.6px; margin-top: 6px; }
</style>
</head>
<body>
<main class="flyer">
  <svg class="backdrop" width="849" height="1200" viewBox="0 0 849 1200">
    <defs>
      <linearGradient id="photo-tone" x1="0" y1="0" x2="1" y2="0">
        <stop offset="0" stop-color="var(--photo-dark)"/>
        <stop offset="0.42" stop-color="#7b7f84"/>
        <stop offset="0.6" stop-color="var(--photo-light)"/>
        <stop offset="1" stop-color="#e4e2e0"/>
      </linearGradient>
      <linearGradient id="floor-tone" x1="0" y1="0" x2="0" y2="1">
        <stop offset="0" stop-color="var(--photo-floor)" stop-opacity="0"/>
        <stop offset="1" stop-color="var(--photo-floor)" stop-opacity="0.9"/>
      </linearGradient>
    </defs>
    <g role="img" aria-label="Photo of a canister carpet-cleaning machine with its hose running across a plush carpet">
      <rect x="0" y="250" width="849" height="830" fill="url(#photo-tone)"/>
      <rect x="380" y="660" width="469" height="420" fill="url(#floor-tone)"/>
    </g>
    <path d="M0 240 Q424 330 849 240 L849 262 Q424 350 0 262 Z" fill="var(--brand-red)"/>
    <path d="M0 0 H849 V240 Q424 330 0 240 Z" fill="var(--ink)"/>
    <path d="M0 1090 Q424 1010 849 1090 V1200 H0 Z" fill="var(--brand-red)"/>
    <path d="M0 1108 Q424 1040 849 1108 V1200 H0 Z" fill="var(--ink)"/>
  </svg>

  <header class="brand">
    <div class="brand-name">MERIDIAN SWIFT</div>
    <div class="brand-tagline">Premium Rug &amp; Home Care</div>
  </header>

  <h1 class="headline">One Stop For All Your Home Cleaning Needs</h1>

  <ul class="services">
    <li class="service">
      <span class="service-icon">
        <svg viewBox="0 0 44 44"><rect x="8" y="12" width="13" height="24" rx="6" fill="#000"/><path d="M14 12 Q16 4 24 6 L32 36" stroke="#000" stroke-width="3" fill="none"/><rect x="27" y="35" width="12" height="4" rx="2" fill="#000"/><circle cx="12" cy="38" r="3" fill="#000"/></svg>
      </span>
      <span class="service-name">Carpet Cleaning</span>
    </li>
    <li class="service">
      <span class="service-icon">
        <svg viewBox="0 0 44 44"><rect x="11" y="9" width="22" height="14" rx="4" fill="#000"/><rect x="5" y="17" width="8" height="15" rx="3" fill="#000"/><rect x="31" y="17" width="8" height="15" rx="3" fill="#000"/><rect x="11" y="24" width="22" height="8" fill="#000"/><rect x="9" y="32" width="3" height="5" fill="#000"/><rect x="32" y="32" width="3" height="5" fill="#000"/></svg>
      </span>
      <span class="service-name">Upholstery Cleaning</span>
    </li>
    <li class="service">
      <span class="service-icon">
        <svg viewBox="0 0 44 44"><rect x="6" y="8" width="10" height="12" fill="#000"/><rect x="6" y="22" width="10" height="12" fill="#000"/><rect x="18" y="8" width="6" height="26" fill="#000"/><path d="M27 6 H38 V38 L32.5 33 L27 38 Z" fill="#000"/></svg>
      </span>
      <span class="service-name">Drapery Cleaning</span>
    </li>
    <li class="service">
      <span class="service-icon">
        <svg viewBox="0 0 44 44" fill="none" stroke="#000" stroke-width="3.2" stroke-linejoin="round"><path d="M8 16 L22 7 L36 16 L22 25 Z"/><path d="M8 26 L22 17 L36 26 L22 35 Z"/></svg>
      </span>
      <span class="service-name">Tile &amp; Grout Cleaning</span>
    </li>
    <li class="service">
      <span class="service-icon">
        <svg viewBox="0 0 44 44"><path d="M10 26 H34 L39 38 H5 Z" fill="#000"/><path d="M22 4 L24 12 L32 14 L24 16 L22 24 L20 16 L12 14 L20 12 Z" fill="#000"/><path d="M34 14 L35 18 L39 19 L35 20 L34 24 L33 20 L29 19 L33 18 Z" fill="#000"/><path d="M9 14 L10 17 L13 18 L10 19 L9 22 L8 19 L5 18 L8 17 Z" fill="#000"/></svg>
      </span>
      <span class="service-name">Natural Stone<br>Cleaning &amp; Polishing</span>
    </li>
  </ul>

  <section class="call">
    <span class="call-icon">
      <svg viewBox="0 0 46 46" fill="none" stroke="#fff" stroke-width="2.4" stroke-linejoin="round" stroke-linecap="round"><path d="M12 8 L18 8 L20 16 L16 19 Q19 26 26 30 L29 26 L37 28 L37 34 Q36 39 31 38 Q13 34 8 15 Q8 9 12 8 Z"/><path d="M26 10 Q33 11 35 18"/><path d="M26 5 Q38 6 40 18"/></svg>
    </span>
    <div class="call-text">
      <div class="call-label">CALL NOW</div>
      <div class="call-number">702-555-0148</div>
    </div>
  </section>

  <aside class="offer">
    <div class="offer-inner">
      <div class="offer-days">30 DAYS</div>
      <div class="offer-sub">SPECIAL OFFER</div>
      <div class="offer-rule"></div>
      <div class="offer-discount">DISCOUNT</div>
      <div class="offer-note">ON NEXT SERVICE!</div>
    </div>
  </aside>

  <footer class="contact">
    <p class="contact-address">4180 W. Sunridge Avenue, Suite C, Las Vegas, Nevada 89103</p>
    <p class="contact-web">www.meridianswiftcleaners.com</p>
  </footer>
</main>
</body>
</html>
```